Educational Management System User Interface (Vantro Design Concepts)

Hi,I require a 1-page design for an educational management system. The image attached shows all required elements and also their locations. I require the design to be based on vantro-styled interfaces using elements from: http://qelvo.hostrun.io/qelvo-kitset/ & http://layoutmintly.com/layout-template/admin . Side menu's should not be too large that they hide the main content of the page.
Sorry very slight addition to the design as per new uploaded file.
I like how the elements of the vantro hub page are seperated with the background colour and white boxes. This could maybe work in the design as per the uploaded image?
Thanks,
Melvin
Reason: Some designers have some submissions.

```html
<!DOCTYPE html>
<html lang="en">
<head>
<meta charset="utf-8">
<title>EDVORA – Teacher Dashboard</title>
<link href="https://fonts.googleapis.com/css2?family=Open+Sans:wght@300;400;600;700&display=swap" rel="stylesheet">
<style>
:root{
  --topbar:#686e7a;
  --topbar-active:#4f5561;
  --topbar-line:#7b818c;
  --sidebar:#35a9dc;
  --sidebar-item:#4bbbe7;
  --sidebar-line:#3aa6d6;
  --sidebar-title:#1c7cab;
  --green:#8cc24c;
  --aside:#e9ecf0;
  --aside-line:#d6dbe1;
  --card:#f3f5f8;
  --card-border:#e3e7ec;
  --text:#5f6670;
  --muted:#9aa1a9;
  --accent:#2a9fd6;
  --alert:#f0654a;
  --timeline:#cfd4da;
  --photo-a:#d8a77a;
  --photo-b:#8a5b3c;
}
*{box-sizing:border-box;margin:0;padding:0}
html,body{width:1024px;height:1200px;overflow:hidden;background:#fff}
body{font-family:"Open Sans",Arial,sans-serif;color:var(--text)}
.page{position:absolute;left:0;top:0;width:1280px;height:1500px;transform:scale(.8);transform-origin:0 0;background:#fff}
.abs{position:absolute}
.photo{position:absolute;background:linear-gradient(160deg,var(--photo-a),var(--photo-b))}

/* top bar */
.topbar{position:absolute;left:0;top:0;width:1280px;height:74px;background:var(--topbar)}
.brand{position:absolute;left:30px;top:18px;font-size:29px;font-weight:700;color:#e3e6ea;letter-spacing:1px}
.nav-cell{position:absolute;top:0;height:74px;border-left:1px solid var(--topbar-line);display:flex;align-items:center;justify-content:center}
.nav-cell.active{background:var(--topbar-active)}
.badge{position:absolute;width:17px;height:17px;border-radius:50%;background:var(--alert);color:#fff;font-size:10px;font-weight:700;text-align:center;line-height:17px}
.user-name{position:absolute;left:1152px;top:27px;color:#fff;font-size:14px}

/* sidebar */
.sidebar{position:absolute;left:0;top:74px;width:224px;height:1426px;background:var(--sidebar)}
.role{position:absolute;left:22px;top:50px;font-size:30px;font-weight:300;color:var(--sidebar-title)}
.side-head{position:absolute;left:22px;display:flex;align-items:center;gap:10px;color:#fff;font-weight:700;font-size:16px;letter-spacing:.5px}
.side-item{position:absolute;left:0;width:224px;height:41px;background:var(--sidebar-item);border-bottom:1px solid var(--sidebar-line);color:#fff;font-size:14px;padding:10px 27px}
.side-btn{position:absolute;left:24px;width:140px;height:34px;background:var(--green);color:#fff;font-size:12px;text-align:center;line-height:34px;border-radius:2px}

/* composer */
.refine{position:absolute;left:755px;top:107px;width:150px;height:36px;border:1px solid var(--card-border);background:#f6f7f9;font-size:14px;padding:8px 12px;color:#555}
.composer{position:absolute;left:355px;top:155px;width:560px;height:35px;border:1px solid #dfe3e8;font-size:14px;color:var(--muted);padding:8px 14px}
.post-btn{position:absolute;left:813px;top:198px;width:90px;height:34px;background:var(--green);border-radius:2px}

/* timeline */
.timeline{position:absolute;left:299px;top:280px;width:2px;height:840px;background:var(--timeline)}
.post{position:absolute;left:355px;width:600px;height:162px;background:var(--card);box-shadow:0 1px 2px rgba(0,0,0,.08)}
.post.reply{left:444px;width:511px;background:#fff;border:1px solid var(--card-border)}
.post::before{content:"";position:absolute;left:-12px;top:56px;border:12px solid transparent;border-left:0;border-right-color:var(--card)}
.post.reply::before{border-right-color:#fff;left:-12px}
.post-author{position:absolute;left:20px;top:24px;font-size:14px;color:#555}
.post-date{position:absolute;right:25px;top:26px;font-size:13px;color:var(--muted)}
.post-body{position:absolute;left:20px;top:56px;right:25px;font-size:14px;line-height:20px;color:#666}
.reply-ico{position:absolute;right:12px;bottom:14px}
.attach{position:absolute;left:20px;top:28px;width:70px;text-align:center;color:var(--accent);font-size:11px;font-weight:600}

/* aside */
.aside{position:absolute;left:990px;top:74px;width:290px;height:1426px;background:var(--aside)}
.aside-title{position:absolute;left:87px;font-size:16px;font-weight:700;color:#6b727b;letter-spacing:.3px}
.event{position:absolute;left:0;width:290px;height:41px;border-bottom:1px solid var(--aside-line);font-size:14px;color:#666;padding:10px 18px;display:flex;align-items:center}
.event .sep{color:#b5bbc2;margin:0 9px}
.event .info{position:absolute;right:13px;top:14px;width:12px;height:12px;border-radius:50%;background:var(--alert);color:#fff;font-size:9px;font-weight:700;text-align:center;line-height:12px}

/* messages dropdown */
.dropdown{position:absolute;left:868px;top:60px;width:233px;height:334px;background:#fff;border:1px solid #dde1e6;box-shadow:0 3px 8px rgba(0,0,0,.15)}
.dd-head{height:40px;border-bottom:1px solid #e6e9ed;font-size:12px;color:#555;padding:13px 11px}
.msg{position:absolute;left:0;width:226px;height:82px;border-bottom:1px solid #e6e9ed;font-size:11px;color:#555;padding:10px}
.msg.hover{background:#f3f5f8}
.msg .who{position:absolute;left:57px;top:12px;color:var(--accent);font-size:12px}
.msg .time{position:absolute;right:10px;top:13px;font-style:italic;font-weight:700;font-size:11px;color:#333}
.msg .l1{position:absolute;left:57px;top:33px}
.msg .l2{position:absolute;left:10px;top:53px;right:8px;white-space:nowrap;overflow:hidden;text-overflow:ellipsis}
.msg .l3{position:absolute;left:10px;top:73px}
.dd-foot{position:absolute;left:10px;top:304px;width:212px;font-size:12px;color:#555;display:flex;justify-content:space-between;align-items:center}
.scroll{position:absolute;right:2px;top:40px;width:4px;height:80px;background:#e1e4e8;border-radius:2px}
</style>
</head>
<body>
<div class="page">

  <header class="topbar">
    <div class="brand">EDVORA</div>
    <div class="nav-cell" style="left:223px;width:76px">
      <svg width="22" height="20" viewBox="0 0 22 20"><path d="M11 1L1 10h3v9h5v-6h4v6h5v-9h3z" fill="#c7ccd3"/></svg>
    </div>
    <div class="nav-cell active" style="left:298px;width:77px">
      <svg width="22" height="18" viewBox="0 0 22 18" fill="none" stroke="#d4d8de" stroke-width="2"><rect x="1" y="1" width="20" height="16"/><path d="M1 6h20M1 11h20M8 1v16M14 1v16"/></svg>
    </div>
    <div class="nav-cell" style="left:375px;width:77px">
      <svg width="22" height="18" viewBox="0 0 22 18"><path d="M2 9l6 6L20 3" stroke="#c7ccd3" stroke-width="4" fill="none"/></svg>
    </div>
    <div class="nav-cell" style="left:451px;width:78px;border-right:1px solid var(--topbar-line)">
      <svg width="22" height="18" viewBox="0 0 22 18"><path d="M1 3h7l2 2h8v3H5L1 16zM5 9h17l-4 8H1z" fill="#c7ccd3"/></svg>
    </div>

    <svg class="abs" style="left:1012px;top:28px" width="24" height="22" viewBox="0 0 24 22"><path d="M12 1L1 21h22z" fill="#8d929b"/></svg>
    <span class="badge" style="left:1008px;top:25px">6</span>
    <svg class="abs" style="left:1062px;top:30px" width="24" height="18" viewBox="0 0 24 18"><rect width="24" height="18" fill="#8d929b"/><path d="M0 0l12 10L24 0" stroke="#686e7a" stroke-width="2" fill="none"/></svg>
    <span class="badge" style="left:1059px;top:25px">5</span>
    <div class="photo" style="left:1112px;top:24px;width:29px;height:29px;--photo-a:#e6e6e6;--photo-b:#7b7b7b" role="img" aria-label="Profile photo of John Doe"></div>
    <div class="user-name">John Doe <span style="color:#9aa0a8;font-size:11px">&#8964;</span></div>
  </header>

  <nav class="sidebar">
    <div class="role">Teacher</div>
    <div class="side-head" style="top:104px">
      <svg width="25" height="22" viewBox="0 0 25 22" fill="none" stroke="#8fd3f2" stroke-width="1.3"><circle cx="12.5" cy="6" r="4"/><path d="M5 21c0-5 3-8 7.5-8s7.5 3 7.5 8"/><circle cx="5" cy="8" r="3"/><circle cx="20" cy="8" r="3"/><path d="M1 19c0-4 2-6 4-6M24 19c0-4-2-6-4-6"/></svg>
      MY GROUPS
    </div>
    <div class="side-item" style="top:144px">Group Name</div>
    <div class="side-item" style="top:185px">Group Name</div>
    <div class="side-item" style="top:226px">Group Name</div>
    <div class="side-item" style="top:267px">Group Name</div>
    <div class="side-btn" style="top:326px">Create New Group</div>
    <div class="side-btn" style="top:366px">Join More Group</div>
    <div class="side-head" style="top:437px">
      <svg width="25" height="24" viewBox="0 0 25 24" fill="none" stroke="#8fd3f2" stroke-width="1.3"><circle cx="12.5" cy="12" r="4"/><circle cx="5" cy="5" r="3"/><circle cx="20" cy="5" r="3"/><circle cx="5" cy="19" r="3"/><circle cx="20" cy="19" r="3"/></svg>
      COMMUNITY
    </div>
    <div class="side-item" style="top:477px;height:42px">Study Owl</div>
  </nav>

  <main>
    <div class="refine">Refine by Group</div>
    <div class="photo" style="left:272px;top:154px;width:64px;height:64px;--photo-a:#c9a58a;--photo-b:#5a4032" role="img" aria-label="Teacher profile photo"></div>
    <div class="composer">Post New Update...</div>
    <svg class="abs" style="left:706px;top:207px" width="14" height="14" viewBox="0 0 14 14" fill="none" stroke="#777" stroke-width="1.6"><circle cx="4" cy="4" r="3"/><circle cx="10" cy="10" r="3"/><path d="M6 6l2 2"/></svg>
    <svg class="abs" style="left:742px;top:207px" width="12" height="14" viewBox="0 0 12 14" fill="none" stroke="#777" stroke-width="1.4"><path d="M1 1h6l4 4v8H1z"/></svg>
    <svg class="abs" style="left:775px;top:208px" width="16" height="13" viewBox="0 0 16 13"><rect y="2" width="16" height="11" rx="1" fill="#777"/><rect x="5" width="6" height="3" fill="#777"/><circle cx="8" cy="7.5" r="3" fill="#fff"/></svg>
    <div class="post-btn"></div>

    <svg class="abs" style="left:288px;top:256px" width="22" height="22" viewBox="0 0 22 22" fill="none" stroke="var(--accent)" stroke-width="3"><path d="M3 10a8 8 0 0 1 15-3M19 12a8 8 0 0 1-15 3"/><path d="M19 2v6h-6M3 20v-6h6" stroke-width="2.4"/></svg>
    <div class="timeline"></div>

    <article class="post" style="top:279px">
      <div class="post-author">Anna Molly</div><div class="post-date">12 Dec, 2014 at 12:10</div>
      <p class="post-body">Cras sit amet nibh libero, in gravida nulla. Nulla vel metus scelerisque ante sollicitudin commodo. Cras purus odio, vestibulum in vulputate at, tempus viverra turpis.</p>
      <svg class="reply-ico" width="14" height="12" viewBox="0 0 14 12"><path d="M6 0L0 5l6 5V7c4 0 6 1 8 5 0-5-3-8-8-8z" fill="var(--accent)"/></svg>
    </article>
    <div class="photo" style="left:268px;top:316px;width:64px;height:64px" role="img" aria-label="Profile photo of Anna Molly"></div>

    <article class="post reply" style="top:452px">
      <div class="post-author" style="left:23px">Anna Molly</div><div class="post-date">12 Dec, 2014 at 12:10</div>
      <p class="post-body" style="left:23px">Cras sit amet nibh libero, in gravida nulla. Nulla vel metus scelerisque ante sollicitudin commodo. Cras purus odio, vestibulum in vulputate at, tempus viverra turpis.</p>
      <svg class="reply-ico" width="14" height="12" viewBox="0 0 14 12"><path d="M6 0L0 5l6 5V7c4 0 6 1 8 5 0-5-3-8-8-8z" fill="var(--accent)"/></svg>
    </article>
    <div class="photo" style="left:360px;top:498px;width:64px;height:64px" role="img" aria-label="Profile photo of Anna Molly"></div>

    <article class="post" style="top:657px">
      <div class="attach">
        <svg width="54" height="66" viewBox="0 0 54 66" fill="none" stroke="#5c6b7a" stroke-width="2.5"><path d="M2 2h34l16 16v46H2z"/><path d="M36 2v16h16"/><circle cx="24" cy="40" r="12"/><path d="M24 40V28M24 40h12"/><path d="M30 34l8-8" /></svg>
        <div>results.pdf</div>
      </div>
      <div class="post-author" style="left:111px">Anna Molly</div><div class="post-date">12 Dec, 2014 at 12:10</div>
      <p class="post-body" style="left:111px">Cras sit amet nibh libero, in gravida nulla. Nulla vel metus scelerisque ante sollicitudin commodo. Cras purus odio, vestibulum in vulputate at, tempus viverra turpis.</p>
      <svg class="reply-ico" width="14" height="12" viewBox="0 0 14 12"><path d="M6 0L0 5l6 5V7c4 0 6 1 8 5 0-5-3-8-8-8z" fill="var(--accent)"/></svg>
    </article>
    <div class="photo" style="left:268px;top:695px;width:64px;height:64px" role="img" aria-label="Profile photo of Anna Molly"></div>

    <article class="post" style="top:877px">
      <div class="post-author">Anna Molly</div><div class="post-date">12 Dec, 2014 at 12:10</div>
      <p class="post-body">Cras sit amet nibh libero, in gravida nulla. Nulla vel metus scelerisque ante sollicitudin commodo. Cras purus odio, vestibulum in vulputate at, tempus viverra turpis.</p>
      <svg class="reply-ico" width="14" height="12" viewBox="0 0 14 12"><path d="M6 0L0 5l6 5V7c4 0 6 1 8 5 0-5-3-8-8-8z" fill="var(--accent)"/></svg>
    </article>
    <div class="photo" style="left:268px;top:915px;width:64px;height:64px" role="img" aria-label="Profile photo of Anna Molly"></div>

    <article class="post" style="top:1085px">
      <div class="post-author">Anna Molly</div><div class="post-date">12 Dec, 2014 at 12:10</div>
      <p class="post-body">Cras sit amet nibh libero, in gravida nulla. Nulla vel metus scelerisque ante sollicitudin commodo. Cras purus odio, vestibulum in vulputate at, tempus viverra turpis.</p>
      <svg class="reply-ico" width="14" height="12" viewBox="0 0 14 12"><path d="M6 0L0 5l6 5V7c4 0 6 1 8 5 0-5-3-8-8-8z" fill="var(--accent)"/></svg>
    </article>
    <div class="photo" style="left:268px;top:1123px;width:64px;height:64px" role="img" aria-label="Profile photo of Anna Molly"></div>

    <article class="post reply" style="top:1259px">
      <div class="post-author" style="left:23px">Anna Molly</div><div class="post-date">12 Dec, 2014 at 12:10</div>
      <p class="post-body" style="left:23px">Cras sit amet nibh libero, in gravida nulla. Nulla vel metus scelerisque ante sollicitudin commodo. Cras purus odio, vestibulum in vulputate at, tempus viverra turpis.</p>
      <svg class="reply-ico" width="14" height="12" viewBox="0 0 14 12"><path d="M6 0L0 5l6 5V7c4 0 6 1 8 5 0-5-3-8-8-8z" fill="var(--accent)"/></svg>
    </article>
    <div class="photo" style="left:360px;top:1305px;width:64px;height:64px" role="img" aria-label="Profile photo of Anna Molly"></div>
  </main>

  <aside class="aside">
    <div class="aside-title" style="top:48px">TODAY'S EVENTS</div>
    <div class="event" style="top:92px">12:15<span class="sep">|</span>Meeting in Canteen<span class="info">i</span></div>
    <div class="event" style="top:133px">12:15<span class="sep">|</span>Meeting in Canteen<span class="info">i</span></div>
    <div class="event" style="top:174px">12:15<span class="sep">|</span>Meeting in Canteen<span class="info">i</span></div>
    <div class="event" style="top:215px">12:15<span class="sep">|</span>Meeting in Canteen<span class="info">i</span></div>
    <div class="event" style="top:256px">12:15<span class="sep">|</span>Meeting in Canteen<span class="info">i</span></div>

    <svg class="abs" style="left:18px;top:331px" width="51" height="53" viewBox="0 0 51 53" fill="none" stroke="#6b727b" stroke-width="2"><rect x="1" y="7" width="49" height="45"/><path d="M1 16h49M10 1v10M18 1v10M26 1v10M34 1v10M42 1v10"/><text x="25.5" y="44" text-anchor="middle" font-family="Open Sans,Arial,sans-serif" font-size="24" fill="#6b727b" stroke="none">25</text></svg>
    <div class="aside-title" style="top:350px">UPCOMING EVENTS</div>
    <div class="event" style="top:394px">12:15<span class="sep">|</span>Meeting in Canteen<span class="info">i</span></div>
    <div class="event" style="top:435px">12:15<span class="sep">|</span>Meeting in Canteen<span class="info">i</span></div>
    <div class="event" style="top:476px">12:15<span class="sep">|</span>Meeting in Canteen<span class="info">i</span></div>
    <div class="event" style="top:517px">12:15<span class="sep">|</span>Meeting in Canteen<span class="info">i</span></div>
    <div class="event" style="top:558px">12:15<span class="sep">|</span>Meeting in Canteen<span class="info">i</span></div>
  </aside>

  <div class="dropdown">
    <div class="dd-head">You have 14 new messages</div>
    <div class="scroll"></div>
    <div class="msg" style="top:40px">
      <div class="photo" style="left:10px;top:10px;width:40px;height:40px;--photo-a:#b07a52;--photo-b:#2e1d14" role="img" aria-label="Photo of Lisa Wong"></div>
      <span class="who">Lisa Wong</span><span class="time">22 mins</span>
      <span class="l1">Vivamus sed auctor nibh</span>
      <span class="l2">congue nibh. auctor nibh auctor nibh auctor</span>
    </div>
    <div class="msg hover" style="top:122px;height:102px">
      <div class="photo" style="left:10px;top:10px;width:40px;height:40px;--photo-a:#d0b8a2;--photo-b:#3f5a3a" role="img" aria-label="Photo of Richard Doe"></div>
      <span class="who">Richard Doe</span><span class="time">22 mins</span>
      <span class="l1">Vivamus sed auctor nibh</span>
      <span class="l2">congue nibh. auctor nibh auctor nibh auctor</span>
      <span class="l3">auctor nibh...</span>
    </div>
    <div class="msg" style="top:224px">
      <div class="photo" style="left:10px;top:10px;width:40px;height:40px;--photo-a:#eeeeee;--photo-b:#555" role="img" aria-label="Photo of Bob Nilson"></div>
      <span class="who">Bob Nilson</span><span class="time">22 mins</span>
      <span class="l1">Vivamus sed auctor nibh</span>
      <span class="l2">congue nibh. auctor nibh auctor nibh auctor</span>
    </div>
    <div class="dd-foot">See all messages
      <svg width="14" height="14" viewBox="0 0 14 14" fill="none" stroke="#555" stroke-width="1.3"><circle cx="7" cy="7" r="6"/><path d="M4 7h6M7.5 4.5L10 7 7.5 9.5"/></svg>
    </div>
  </div>

</div>
</body>
</html>
```